Business Card Design

My husband & I have a singing business so just need a card with my husband's photo on it and our current logo. I have attached the logo on the top of a page plus a photo of my husband & our theme colour we would like is a black background with red writing to match our logo. If you can please also put somewhere on the card "Entertainment for any occasion inc. Pubs, Clubs, Birthday Parties or Weddings". The photo is on the poster attached if you are able to copy it please.

Industry/Entity Type

Business

Contact Information for Business Card

Marty & Jen Ashcroft
Mobile: 0438 926 341
Email: jenna.pruett@mailverge.com

```html
<!DOCTYPE html>
<html lang="en">
<head>
<meta charset="utf-8">
<title>Velvet Echo Entertainment – Business Card</title>
<link href="https://fonts.googleapis.com/css2?family=Questrial&display=swap" rel="stylesheet">
<style>
  :root {
    --page-bg: #e9e9e6;
    --card-black: #0d0d0d;
    --card-charcoal: #2a2a2a;
    --band-warm: #efe2a2;
    --band-cool: #dcefc9;
    --brand-red: #d42a24;
    --tag-red: #e0322c;
    --tag-cream: #f1e3a6;
    --ink-dark: #2b2b2b;
    --photo-skin: #8a5a45;
    --photo-shadow: #2a1c17;
  }
  * { margin: 0; padding: 0; box-sizing: border-box; }
  html, body {
    width: 1200px;
    height: 970px;
    overflow: hidden;
    background: var(--page-bg);
    font-family: "Questrial", "Century Gothic", sans-serif;
  }
  .business-card {
    position: absolute;
    left: 100px;
    top: 200px;
    width: 1000px;
    height: 570px;
    border-radius: 26px;
    overflow: hidden;
    background: linear-gradient(90deg, var(--band-warm) 0%, var(--band-cool) 70%);
    box-shadow: 0 10px 30px rgba(0,0,0,0.25);
  }
  .card-shapes {
    position: absolute;
    inset: 0;
    width: 1000px;
    height: 570px;
  }
  .brand {
    position: absolute;
    left: 150px;
    top: 70px;
    display: flex;
    align-items: center;
    gap: 18px;
  }
  .brand-dot {
    width: 34px;
    height: 34px;
    border-radius: 50%;
    background: var(--brand-red);
  }
  .brand-name {
    color: var(--brand-red);
    font-size: 46px;
    line-height: 1.05;
    font-weight: 400;
  }
  .tagline {
    position: absolute;
    left: 127px;
    top: 222px;
    font-size: 26px;
    line-height: 32px;
    letter-spacing: 0.3px;
  }
  .tagline-lead { color: var(--tag-red); }
  .tagline-venues { color: var(--tag-cream); }
  .owners {
    position: absolute;
    left: 44px;
    top: 400px;
    color: var(--ink-dark);
    font-size: 43px;
    letter-spacing: 0.5px;
  }
  .contact-row {
    position: absolute;
    left: 44px;
    top: 455px;
    display: flex;
    align-items: center;
    color: var(--ink-dark);
    font-size: 27px;
  }
  .contact-item { display: flex; align-items: center; gap: 12px; }
  .contact-item + .contact-item { margin-left: 30px; }
  .contact-icon { width: 26px; height: 22px; fill: var(--brand-red); }
  .portrait {
    position: absolute;
    left: 705px;
    top: 180px;
    width: 295px;
    height: 390px;
    border-radius: 48% 48% 0 0 / 34% 34% 0 0;
    background: radial-gradient(ellipse at 45% 40%, var(--photo-skin) 0%, #6b4434 45%, var(--photo-shadow) 100%);
  }
</style>
</head>
<body>
  <div class="business-card">
    <svg class="card-shapes" viewBox="0 0 1000 570" aria-hidden="true">
      <defs>
        <linearGradient id="top-black" x1="0" y1="0" x2="1" y2="1">
          <stop offset="0" stop-color="#1c1c1c"/>
          <stop offset="0.5" stop-color="#070707"/>
          <stop offset="1" stop-color="#222222"/>
        </linearGradient>
      </defs>
      <path d="M0,0 H1000 V330 C850,352 700,348 500,338 S150,318 0,322 Z" fill="url(#top-black)"/>
      <path d="M0,570 V548 C300,522 600,512 1000,528 V570 Z" fill="var(--card-black)"/>
    </svg>

    <div class="brand">
      <span class="brand-dot"></span>
      <span class="brand-name">Velvet Echo<br>Entertainment</span>
    </div>

    <p class="tagline">
      <span class="tagline-lead">Entertainment for any occasion inc</span><br>
      <span class="tagline-venues">Pubs, Clubs, Birthday Parties or Weddings</span>
    </p>

    <div class="portrait" role="img" aria-label="Portrait photo of the lead singer"></div>

    <h1 class="owners">Marty &amp; Jen Ashcroft</h1>

    <div class="contact-row">
      <span class="contact-item">
        <svg class="contact-icon" viewBox="0 0 26 22" aria-hidden="true">
          <path d="M2,7 C2,3 6,1 13,1 C20,1 24,3 24,7 L24,9 L18,9 L18,6 L8,6 L8,9 L2,9 Z"/>
          <path d="M7,10 L19,10 L23,20 L3,20 Z"/>
        </svg>
        0438 926 341
      </span>
      <span class="contact-item">
        <svg class="contact-icon" viewBox="0 0 26 22" aria-hidden="true">
          <path d="M1,3 H25 V19 H1 Z M3,5 L13,12 L23,5" stroke="#f4ecc8" stroke-width="1.6"/>
        </svg>
        jenna.pruett@mailverge.com
      </span>
    </div>
  </div>
</body>
</html>
```